Allied Health Clinic needs catchy poster ad for lightbox

We need a catchy and effective poster designed for our retail lightbox which is in a busy corridor. We are a multi disciplinary sports injury clinic offering a range of allied health services. Established in 1999. We need people to understand our business identity and services clearly. I have come up with a very rough idea as far as what I think the copy should contain. The picture is an example of what image I am trying to convey to the potential client. I am not a designer clearly. We specialise in treating difficult problems.
Size of the poster is 451mm x 741mm at 300dpi. We will then blow the image up to double this size which will be good enough resolution for the printing.

Target Market(s)

White collar professionals - male and female, active 20-50 range

Industry/Entity Type

Healthcare

Font styles to use
Sans Serif

Requirements
Nice to have
• Easy to read, polished, nice tie in to my logo colours

```html
<!DOCTYPE html>
<html lang="en">
<head>
<meta charset="utf-8">
<title>Injury Experts – Lightbox Poster</title>
<link rel="stylesheet" href="https://fonts.googleapis.com/css2?family=Roboto+Condensed:wght@400;700&display=swap">
<style>
  :root {
    --green: #8cc63f;
    --ink: #111111;
    --charcoal: #4a4a4c;
    --band-dark: #4b4b4d;
    --band-light: #dcdcde;
    --paper: #ffffff;
    --backdrop: #e4e5e7;
  }
  * { margin: 0; padding: 0; box-sizing: border-box; }
  html, body {
    width: 933px; height: 1200px; overflow: hidden;
    background: var(--backdrop);
    font-family: "Roboto Condensed", "Arial Narrow", sans-serif;
  }
  .poster {
    position: absolute; left: 120px; top: 20px;
    width: 692px; height: 1161px;
    background: var(--paper);
    overflow: hidden;
    box-shadow: 0 6px 24px rgba(0,0,0,.18);
  }
  .poster-shapes { position: absolute; inset: 0; }
  .txt { position: absolute; line-height: 1; font-weight: 700; white-space: nowrap; text-transform: uppercase; }

  .headline { color: var(--green); }
  .headline-injury { left: 57px; top: 11px; font-size: 108px; letter-spacing: -1px; }
  .headline-experts { left: 58px; top: 106px; font-size: 76px; letter-spacing: -0.5px; }

  .tagline { left: 56px; top: 196px; color: var(--charcoal); font-size: 37px; line-height: 44px; transform: rotate(-4deg); transform-origin: left top; }

  .claim { left: 60px; color: var(--ink); }
  .claim-1 { top: 382px; font-size: 32px; }
  .claim-2 { top: 424px; font-size: 37px; }
  .claim-3 { top: 471px; font-size: 37px; }
  .claim-4 { top: 517px; font-size: 37px; }
  .claim-since { top: 558px; font-size: 22px; }

  .range { left: 62px; color: var(--ink); font-size: 31px; }
  .range-1 { top: 624px; }
  .range-2 { top: 663px; }

  .service { color: var(--paper); font-size: 29px; }

  .clinic-name { left: 45px; color: var(--charcoal); font-weight: 400; }
  .clinic-name-main { top: 1006px; font-size: 25px; letter-spacing: 1.6px; }
  .clinic-name-sub { top: 1033px; font-size: 13px; letter-spacing: 6px; }

  .contact { right: 21px; color: var(--paper); text-align: right; }
  .contact-lifts { top: 1075px; font-size: 29px; }
  .contact-line { top: 1107px; font-size: 33px; text-transform: none; }
</style>
</head>
<body>
  <main class="poster">
    <svg class="poster-shapes" viewBox="0 0 692 1161" width="692" height="1161">
      <defs>
        <linearGradient id="photoTone" x1="0" y1="0" x2="1" y2="1">
          <stop offset="0" stop-color="#f3f4f6"/>
          <stop offset="0.6" stop-color="#dfe2e8"/>
          <stop offset="1" stop-color="#c3c8d3"/>
        </linearGradient>
      </defs>
      <rect class="athlete-photo" x="250" y="20" width="442" height="680" fill="url(#photoTone)" role="img" aria-label="Photo: footballer in navy kit mid-air kicking a soccer ball"/>
      <path class="swoosh-light" d="M27,687 Q420,800 692,500 L692,560 Q420,840 27,687 Z" fill="var(--band-light)"/>
      <path class="swoosh-dark" d="M27,687 Q420,830 692,553 L692,968 C600,995 420,985 260,925 C180,880 110,790 27,687 Z" fill="var(--band-dark)"/>
      <g class="service-bullets" fill="var(--green)">
        <circle cx="113" cy="781" r="13"/>
        <circle cx="154" cy="824" r="13"/>
        <circle cx="203" cy="868" r="13"/>
        <circle cx="267" cy="910" r="13"/>
        <circle cx="356" cy="951" r="13"/>
      </g>
      <path class="footer-band" d="M0,1161 L0,1147 Q330,1050 692,1059 L692,1161 Z" fill="var(--green)"/>
    </svg>

    <h1 class="txt headline headline-injury">Injury</h1>
    <p class="txt headline headline-experts">Experts</p>
    <p class="txt tagline">Trusted<br>by athletes</p>

    <p class="txt claim claim-1">Successfully</p>
    <p class="txt claim claim-2">Treating</p>
    <p class="txt claim claim-3">Difficult</p>
    <p class="txt claim claim-4">Injuries</p>
    <p class="txt claim claim-since">Since 1999</p>

    <p class="txt range range-1">A complete</p>
    <p class="txt range range-2">range of services</p>

    <p class="txt service" style="left:137px;top:767px">Sports Physiotherapy</p>
    <p class="txt service" style="left:178px;top:810px">Chiropractic</p>
    <p class="txt service" style="left:227px;top:854px">Massage</p>
    <p class="txt service" style="left:291px;top:896px">Podiatry</p>
    <p class="txt service" style="left:380px;top:937px">Exercise Physiology</p>

    <p class="txt clinic-name clinic-name-main">Corestride Physiotherapy</p>
    <p class="txt clinic-name clinic-name-sub">&amp; Sports Injury Clinic</p>

    <p class="txt contact contact-lifts">Take lifts to level 8</p>
    <p class="txt contact contact-line">8700 4521&nbsp; | &nbsp;corestridephysio.com.au</p>
  </main>
</body>
</html>
```